Darrow Consulting needs a quality & professional business card!

I am a recruitment and employment consultant from Brisbane, Australia and I had a fantastic logo organised by this community to I am hoping the business card will be the same.

I have attached the Darrow consulting logo that ideally would feature on the back of the business card. There are a number of logos for you to use as you see fit. I would like the colour cheme to match that of the Darrow Consulting logo. I also have a secondary company called Career Lantern Australia and I have included that logo as well. While it is an important part of the business I don't want this logo feature too predominantly as I am moving out of this space. This logo was created by myself and is of low quality. Feel free to use the icon and words however you want. The winning design will be smart, professional and eye-catching.

The information I am looking for in the business card is:
Name: Gavin Darrow
Position: Founder & Director
Phone: (07) 3519 6482
Mobile: 0431 586 207
Email: gavin@careerlantern.com.au

Target Market(s)

Recruiters, government, large companies

Contact Information for Business Card

Name: Gavin Darrow
Phone: (07) 3519 6482
Mobile: 0431 586 207
Web: www.careerlantern.com.au

Font styles to use
Serif
Sans Serif

Requirements
Must have
• Darrow Consulting Logo on reverse side
• Contact details on front side with smaller reference to Darrow Consulting logo and Career Lantern Australia logo

```html
<!DOCTYPE html>
<html lang="en">
<head>
<meta charset="utf-8">
<title>Gavin Darrow – Business Card</title>
<link rel="stylesheet" href="https://fonts.googleapis.com/css2?family=Merriweather:wght@700&family=Roboto+Condensed:wght@400;700&family=Roboto:wght@300;400&display=swap">
<style>
  :root {
    --backdrop: #e9e7e3;
    --card-white: #fbfbfb;
    --card-dark: #1c1e1f;
    --ink: #1e1e1e;
    --ink-soft: #555555;
    --accent-blue: #1aa3d9;
    --rule: #3a3a3a;
    --paper-white: #ffffff;
  }
  * { box-sizing: border-box; margin: 0; padding: 0; }
  html, body { width: 1200px; height: 886px; overflow: hidden; }
  body {
    background: var(--backdrop);
    display: flex;
    align-items: center;
    justify-content: center;
    gap: 60px;
  }
  .card {
    position: relative;
    width: 520px;
    height: 298px;
    border-radius: 2px;
    box-shadow: 0 6px 18px rgba(0,0,0,.18);
  }

  /* Front */
  .card--front { background: var(--card-white); color: var(--ink); }
  .brand {
    position: absolute;
    top: 46px;
    right: 54px;
    display: flex;
    align-items: center;
    gap: 12px;
  }
  .brand__dot {
    width: 34px; height: 34px;
    border-radius: 50%;
    background: var(--ink);
  }
  .brand__name {
    font-family: "Merriweather", Georgia, serif;
    font-weight: 700;
    font-size: 24px;
    line-height: 1;
    color: var(--ink);
  }
  .brand__sub {
    display: block;
    font-family: "Merriweather", Georgia, serif;
    font-weight: 700;
    font-size: 12px;
    margin-top: 4px;
    color: var(--ink);
  }
  .identity {
    position: absolute;
    left: 38px;
    bottom: 34px;
    font-family: "Roboto Condensed", Arial, sans-serif;
    text-transform: uppercase;
  }
  .identity__name { font-weight: 700; font-size: 19px; color: var(--ink); letter-spacing: .2px; }
  .identity__role { font-size: 15px; color: var(--accent-blue); margin-top: 2px; }
  .divider {
    position: absolute;
    left: 228px;
    bottom: 26px;
    width: 1px;
    height: 62px;
    background: var(--rule);
  }
  .contacts {
    position: absolute;
    left: 246px;
    bottom: 30px;
    list-style: none;
    font-family: "Roboto", Arial, sans-serif;
    font-weight: 300;
    font-size: 13px;
    color: var(--ink-soft);
    line-height: 19px;
  }
  .contacts li { display: flex; align-items: center; gap: 8px; }
  .contacts svg { width: 11px; height: 11px; fill: var(--ink); flex: none; }

  /* Back */
  .card--back {
    background: var(--card-dark);
    color: var(--paper-white);
    display: flex;
    align-items: center;
    justify-content: center;
  }
  .back-brand { display: flex; align-items: center; gap: 14px; }
  .back-brand__square { width: 22px; height: 22px; background: var(--paper-white); }
  .back-brand__name {
    font-family: "Merriweather", Georgia, serif;
    font-weight: 700;
    font-size: 26px;
    color: var(--paper-white);
  }
  .web {
    position: absolute;
    left: 22px;
    top: 50%;
    transform: translateY(-50%) rotate(180deg);
    writing-mode: vertical-rl;
    font-family: "Roboto", Arial, sans-serif;
    font-weight: 300;
    font-size: 11px;
    letter-spacing: 4px;
    color: var(--paper-white);
  }
</style>
</head>
<body>
  <section class="card card--front" aria-label="Business card front">
    <div class="brand">
      <span class="brand__dot"></span>
      <div class="brand__name">Career Lantern<span class="brand__sub">Australia</span></div>
    </div>

    <div class="identity">
      <p class="identity__name">Gavin Darrow</p>
      <p class="identity__role">Founder &amp; Director</p>
    </div>

    <span class="divider"></span>

    <ul class="contacts">
      <li>
        <svg viewBox="0 0 12 12" aria-hidden="true"><path d="M2.4 1l2 2.2-1 1.2c.7 1.5 1.8 2.6 3.2 3.3l1.2-1 2.2 2-1.2 1.8C5.4 10.3 1.7 6.6 1 3.2z"/></svg>
        (07) 3519 6482
      </li>
      <li>
        <svg viewBox="0 0 12 12" aria-hidden="true"><path d="M3 0.5h6v11H3zM4 1.5v8h4v-8z"/></svg>
        0431 586 207
      </li>
      <li>
        <svg viewBox="0 0 12 12" aria-hidden="true"><path d="M0.5 2h11v8h-11zM1.5 3v.5L6 6.5l4.5-3V3zM1.5 4.7V9h9V4.7L6 7.7z"/></svg>
        gavin@careerlantern.com.au
      </li>
    </ul>
  </section>

  <section class="card card--back" aria-label="Business card back">
    <p class="web">www.careerlantern.com.au</p>
    <div class="back-brand">
      <span class="back-brand__square"></span>
      <span class="back-brand__name">Darrow Consulting</span>
    </div>
  </section>
</body>
</html>
```